Sign Shop website

We need a web design for a sign company called Quillby Signs that builds signs for shops such as A Frames, Banners, Tennet Boards, Shop front windows etc...

The existing site is avaliable at www.quillbysigns.com.au

We will need to have a fresh makeover. The new site must have the following:

Photo Galleries (broken down into sections)
Store Locations (currently there are 4 stores)
Online quote form
List of services
About Us Page

We just need to front page designed in photoshop (the inner page is not necessary) We have a team that can code the site up.

The website should have the exact logo. Any person who alters the logo, design will be elimated.

No Twitter, RSS, LinkedIn icons

The main colours are yellow, black, blue, red

Target Market(s)

Any business

Industry/Entity Type

It Company

Requirements
Must have
• jQuery slider banner
Should not have
• Alter the logo in any way

```html
<!DOCTYPE html>
<html lang="en">
<head>
<meta charset="utf-8">
<title>Quillby Signs</title>
<link rel="stylesheet" href="https://fonts.googleapis.com/css2?family=Yanone+Kaffeesatz:wght@400;600;700&family=Ubuntu:wght@400;500&display=swap">
<style>
:root{
  --yellow:#edb133;
  --red:#cc3a1a;
  --dark:#2b2b2b;
  --darker:#1a1a1a;
  --black:#0c0c0c;
  --light:#efefef;
  --text:#222;
  --navy:#123a6e;
}
*{margin:0;padding:0;box-sizing:border-box}
html,body{width:1200px;height:1196px;overflow:hidden}
body{position:relative;font-family:"Ubuntu",sans-serif;color:var(--text);background:var(--light)}
.abs{position:absolute}
.head-font{font-family:"Yanone Kaffeesatz",sans-serif;font-weight:700}

/* header */
.site-header{left:0;top:0;width:1200px;height:99px;background:var(--yellow);border-bottom:3px solid var(--red)}
.brand{left:173px;top:22px;display:flex;align-items:center;gap:10px;font-family:"Yanone Kaffeesatz",sans-serif;font-weight:700;font-size:44px;color:var(--red);line-height:1}
.brand-dot{width:22px;height:22px;border-radius:50%;background:var(--red)}
.call{left:876px;top:10px;font-family:"Yanone Kaffeesatz",sans-serif;font-weight:600;font-size:20px;line-height:21px;color:#3a2a10;padding-right:10px;border-right:1px solid #3a2a10}
.call-phone{left:924px;top:18px;font-family:"Yanone Kaffeesatz",sans-serif;font-weight:600;font-size:19px;color:#3a2a10}
.main-nav{left:596px;top:57px;height:39px;display:flex;align-items:center;font-family:"Yanone Kaffeesatz",sans-serif;font-weight:600;font-size:17px;color:#5a2a10}
.main-nav a{color:inherit;text-decoration:none;padding:0 8px}
.main-nav .active{background:var(--red);color:#ffd580;height:39px;line-height:41px;padding:0 15px;border-radius:6px 6px 0 0;margin-right:2px}

/* hero */
.hero{left:0;top:99px;width:1200px;height:370px;background:radial-gradient(ellipse at 35% 40%,#3d3d3d,#242424 70%)}
.hero-title{left:173px;top:160px;font-size:33px;color:var(--yellow)}
.hero-copy{left:174px;top:206px;width:245px;font-size:14px;line-height:18.2px;color:#fff}
.slider-tabs{left:477px;top:234px;width:39px;height:98px;background:var(--red);border-radius:6px 0 0 6px}
.slider-tabs span{position:absolute;left:13px;width:13px;height:13px;border-radius:50%;background:#fff}
.slider-tabs span.on{background:var(--yellow)}
.hero-slide{left:516px;top:117px;width:511px;height:332px;border-radius:6px;
  background:radial-gradient(ellipse 60% 55% at 30% 70%,#6fc6ff 0%,#2a6fd0 28%,#143c8f 55%,#0a1b45 100%)}

/* white section */
.sec-title{font-size:23px;color:var(--dark)}
.sec-title em{font-style:normal;color:var(--red)}
.welcome-photo{left:173px;top:516px;width:188px;height:115px;background:linear-gradient(160deg,#f4f5f6 0%,#d9dcde 45%,#6e7479 100%)}
.welcome-copy{left:376px;top:516px;width:348px;font-size:11px;line-height:16px;text-align:justify}
.btn{background:var(--red);color:#fff;font-family:"Yanone Kaffeesatz",sans-serif;font-weight:600;font-size:14px;border-radius:4px;display:flex;align-items:center;justify-content:center}
.divider{left:173px;top:645px;width:551px;height:1px;background:#c9c9c9}
.services-bg{left:173px;top:646px;width:232px;height:210px;background:linear-gradient(90deg,var(--light),#dcdcdc)}
.service-list{left:173px;top:692px;list-style:none;font-size:12.5px}
.service-list li{height:21.3px;display:flex;align-items:center;gap:10px}
.service-list svg{flex:none}
.person{left:404px;top:658px;width:33px;height:191px;border-radius:14px;background:linear-gradient(#7bb5d8,#5d86ad)}
.map{left:461px;top:690px;width:263px;height:152px;border:1px solid #c8c8c8;background:linear-gradient(135deg,#f1ecdf 0%,#e6dfcb 50%,#efe9d6 100%)}

/* quote */
.quote{left:760px;top:487px;width:267px;height:355px;background:var(--yellow);border-radius:6px;overflow:hidden}
.quote .sec-title{position:absolute;left:17px;top:12px}
.quote label{position:absolute;left:17px;font-size:12px;color:#3a2a10}
.quote .req{position:absolute;left:82px;color:var(--red);font-size:11px}
.field{position:absolute;left:93px;width:156px;height:22px;background:#fff;border-radius:4px;border:1px solid #e3c070}
.select-cap{position:absolute;right:3px;top:3px;width:15px;height:14px;background:var(--yellow);border-radius:3px}
.quote-corner{left:0;bottom:0;width:42px;height:42px;background:linear-gradient(135deg,transparent 50%,var(--dark) 50%)}

/* carousel */
.partners{left:0;top:867px;width:1200px;height:137px;background:linear-gradient(#c9c9c9,#e2e2e2)}
.tile{top:14px;width:177px;height:110px;background:#fff;display:flex;align-items:center;justify-content:center}
.arrow{top:49px;width:36px;height:36px;border-radius:50%;background:var(--yellow)}
.badge-a{width:80px;height:44px;border-radius:8px;background:linear-gradient(135deg,var(--red),#2f4fa0)}
.badge-b{width:120px;height:40px;background:var(--navy)}
.badge-c{width:90px;height:90px;border-radius:50%;border:10px solid #d8202a}

/* footer */
.stores{left:0;top:1004px;width:1200px;height:135px;background:var(--darker);border-top:3px solid var(--yellow)}
.notch{top:0;width:0;height:0;border-left:10px solid transparent;border-right:10px solid transparent;border-top:8px solid var(--yellow)}
.store{top:24px;color:#fff;font-size:12.5px;line-height:16px}
.store h3{font-family:"Yanone Kaffeesatz",sans-serif;font-weight:700;font-size:19px;color:var(--yellow);margin-bottom:9px;line-height:20px}
.store h3 em{font-style:normal;color:var(--red)}
.copyright{left:0;top:1139px;width:1200px;height:57px;background:var(--black);color:var(--yellow);font-size:12.5px;padding:18px 0 0 176px}
</style>
</head>
<body>

<header class="abs site-header">
  <div class="abs brand"><span class="brand-dot"></span>Quillby Signs</div>
  <div class="abs call">CALL<br>NOW</div>
  <div class="abs call-phone">(08) 5550 1234</div>
  <nav class="abs main-nav">
    <a class="active" href="#">HOME</a>
    <a href="#">ABOUT US</a><span>|</span>
    <a href="#">OUR SERVICES</a><span>|</span>
    <a href="#">OUR PORTFOLIO</a><span>|</span>
    <a href="#">CONTACT US</a>
  </nav>
</header>

<section class="abs hero"></section>
<h1 class="abs hero-title head-font">SIGN SOLUTIONS</h1>
<p class="abs hero-copy">Lorem Ipsum is simply dummy text of the printing and typesetting industry. Lorem Ipsum has been the industry's standard dummy text ever since the 1500s, when an unknown printer took a galley of type and scrambled it to make a type specimen book. It has survived not only five centuries, but also the leap into electronic typesetting, remaining essentially unchanged.</p>
<div class="abs slider-tabs"><span style="top:10px"></span><span class="on" style="top:31px"></span><span style="top:52px"></span><span style="top:73px"></span></div>
<div class="abs hero-slide" role="img" aria-label="Night street photo with a danger sign on a roadside board and blue light trails"></div>

<h2 class="abs sec-title head-font" style="left:173px;top:480px">WELCOMR TO <em>QUILLBY SIGNS</em></h2>
<div class="abs welcome-photo" role="img" aria-label="Photo of a lettered sign panel on a white vehicle"></div>
<p class="abs welcome-copy">Quillby Signs is a West Australian owned and managed company. We manufacture signage for any application; vinyl lettering, pull up banners, vehicle signage, in fact anything that requires our customers seeing the full picture when it comes to advertising their business. So if you're serious about the best, put us to the test!</p>
<div class="abs btn" style="left:651px;top:604px;width:73px;height:26px">READ MORE</div>
<div class="abs divider"></div>

<div class="abs services-bg"></div>
<h2 class="abs sec-title head-font" style="left:173px;top:652px">OUR <em>SERVICES</em></h2>
<ul class="abs service-list">
  <li><svg width="9" height="12" viewBox="0 0 9 12"><path d="M1 1l5 5-5 5" fill="none" stroke="#222" stroke-width="2"/></svg>Quality Stickers &amp; Decals</li>
  <li><svg width="9" height="12" viewBox="0 0 9 12"><path d="M1 1l5 5-5 5" fill="none" stroke="#222" stroke-width="2"/></svg>All Sign Types</li>
  <li><svg width="9" height="12" viewBox="0 0 9 12"><path d="M1 1l5 5-5 5" fill="none" stroke="#222" stroke-width="2"/></svg>Vehicle Signage</li>
  <li><svg width="9" height="12" viewBox="0 0 9 12"><path d="M1 1l5 5-5 5" fill="none" stroke="#222" stroke-width="2"/></svg>Magnets</li>
  <li><svg width="9" height="12" viewBox="0 0 9 12"><path d="M1 1l5 5-5 5" fill="none" stroke="#222" stroke-width="2"/></svg>Construction and safety Signs</li>
  <li><svg width="9" height="12" viewBox="0 0 9 12"><path d="M1 1l5 5-5 5" fill="none" stroke="#222" stroke-width="2"/></svg>Window Signage</li>
  <li><svg width="9" height="12" viewBox="0 0 9 12"><path d="M1 1l5 5-5 5" fill="none" stroke="#222" stroke-width="2"/></svg>Laminating</li>
</ul>
<div class="abs person" role="img" aria-label="Photo of a person leaning out from behind the services panel"></div>

<h2 class="abs sec-title head-font" style="left:461px;top:652px">SITE <em>MAP</em></h2>
<div class="abs map" role="img" aria-label="Street map showing the store location"></div>

<form class="abs quote">
  <h2 class="sec-title head-font">QUICK <em>QUOTE</em></h2>
  <label style="top:51px">Name</label><span class="req" style="top:50px">*</span><div class="field" style="top:45px"></div>
  <label style="top:80px">Email</label><span class="req" style="top:79px">*</span><div class="field" style="top:74px"></div>
  <label style="top:109px">Phone</label><span class="req" style="top:108px">*</span><div class="field" style="top:103px"></div>
  <label style="top:139px">Services</label><span class="req" style="top:138px">*</span><div class="field" style="top:133px"><span class="select-cap"></span></div>
  <label style="top:168px">Comment</label><span class="req" style="top:167px">*</span><div class="field" style="top:163px;height:130px"></div>
  <div class="abs btn" style="left:176px;top:307px;width:73px;height:26px">SUBMIT</div>
  <div class="abs quote-corner"></div>
</form>

<section class="abs partners">
  <div class="abs arrow" style="left:173px"><svg width="36" height="36" viewBox="0 0 36 36"><path d="M21 11l-8 7 8 7z" fill="#fff"/></svg></div>
  <div class="abs tile" style="left:222px"><div class="badge-a" role="img" aria-label="Partner panel company badge"></div></div>
  <div class="abs tile" style="left:415px"><div class="badge-b" role="img" aria-label="Partner conveyancing company badge"></div></div>
  <div class="abs tile" style="left:608px;background:linear-gradient(#d9772a 0%,#eeeeee 35%,#c9ccd0 100%)" role="img" aria-label="Photo of a signwritten ute tailgate"></div>
  <div class="abs tile" style="left:800px"><div class="badge-c" role="img" aria-label="No smoking safety sign"></div></div>
  <div class="abs arrow" style="left:990px"><svg width="36" height="36" viewBox="0 0 36 36"><path d="M15 11l8 7-8 7z" fill="#fff"/></svg></div>
</section>

<footer class="abs stores">
  <span class="abs notch" style="left:270px"></span>
  <span class="abs notch" style="left:483px"></span>
  <span class="abs notch" style="left:697px"></span>
  <span class="abs notch" style="left:910px"></span>
  <div class="abs store" style="left:174px"><h3>STORE <em>LOCATION 1</em></h3>Harbourview (08) 5550 1234<br>Ridgemont (08) 5550 5678<br>Lakeside Vale</div>
  <div class="abs store" style="left:386px"><h3>STORE <em>LOCATION 2</em></h3>Harbourview (08) 5550 1234<br>Ridgemont (08) 5550 5678<br>Lakeside Vale</div>
  <div class="abs store" style="left:600px"><h3>STORE <em>LOCATION 3</em></h3>Harbourview (08) 5550 1234<br>Ridgemont (08) 5550 5678<br>Lakeside Vale</div>
  <div class="abs store" style="left:813px"><h3>STORE <em>LOCATION 4</em></h3>Harbourview (08) 5550 1234<br>Ridgemont (08) 5550 5678<br>Lakeside Vale</div>
</footer>
<div class="abs copyright">© 2010 All Right Reserved By Quillby Signs</div>

</body>
</html>
```